have uploaded pics of actual products I will use,here goes
Flapnora
honey butter complete mix 7.75 once $1.69
complete pancake mix 5.1 ounce $2.49
Milk
whole $4.44
C
Moonvessel coffee
medium blend 2.5 ounce $2.99
Qavo sugar
22 ounce pour container $3.49
Tarrowin's cereal
sold by the eaches
$1.29 each
any variety
Apple juice
pelby's 86 ounce bottle
(picture shows 2 bottles of 86 ounce juice)
Pelby's applesauce 3 pack 3 four ounce cups per pack
(picstues show 36 count in back, beeds edite)
Felix dorran turkey bacon 12 ounce pack $3.25
lantern coffee 2.5 ounce $2.50
whitlos eggnog one quart $2.99
rusty vale pre cooked hot and spicy 8 count 9.6 oz $4.49
rusty vale lnks 12 count 10 oz $4.49
Quenby silver crest 1 pound $7.98
Tarrowin fun size cereal 8 count 8.56oz $4.15
tillers gallon milk $4.44
whole, 1% and 2%
whitlos o.j 1 gallon $5.29 128 oz
verelle yogurt 6 oz
peach .69 each
strawberry .69 each
Halverton cinnamon rolls 5 count 7.3 ounce $1.99
Halverton plumps 5 big biscuits 10.2 oz $1.99
zelco hollow brook sharp 8 oz $3.99
zelco sharp shredded cheddar 8 oz $2.99
whitlos half and half 16 ounce $2.49
Thanks!
flyer and business card (which I would like to double as refrigerator magnet. should I increase money to $200 or leave at $150 and offer $50 for second place?
would appreciate all comments
maybe red or yellow
you want flyer or card ?

```html
<!DOCTYPE html>
<html lang="en">
<head>
<meta charset="utf-8">
<title>The Dairy Sprite – Flyer</title>
<link href="https://fonts.googleapis.com/css2?family=Source+Sans+3:ital,wght@0,400;0,600;0,700;1,400;1,700&display=swap" rel="stylesheet">
<style>
  :root {
    --paper: #ffffff;
    --sun-light: #ffd21a;
    --sun-deep: #f6a800;
    --berry: #d8141f;
    --berry-dark: #b50d17;
    --star: #ffe100;
    --ink-blue: #1b3a8c;
    --list-blue: #3c64a3;
    --box-border: #c9a400;
    --white: #ffffff;
  }
  * { margin: 0; padding: 0; box-sizing: border-box; }
  html, body { width: 1200px; height: 874px; overflow: hidden; background: var(--paper); }
  body { font-family: "Source Sans 3", Arial, sans-serif; position: relative; }

  .format-label {
    position: absolute; top: 12px; left: 0; width: 1200px;
    text-align: center; font-size: 34px; color: #111;
  }

  .flyer {
    position: absolute; left: 0; top: 103px; width: 1200px; height: 771px;
    background: radial-gradient(ellipse at 55% 60%, var(--sun-light) 0%, #ffc20e 55%, var(--sun-deep) 100%);
    overflow: hidden;
  }
  .flyer-swoosh { position: absolute; left: 0; top: 0; }

  .mascot-art {
    position: absolute; left: 48px; top: 215px; width: 400px; height: 500px;
    border-radius: 48% 48% 40% 40%;
    background: radial-gradient(circle at 55% 40%, #6fbf7e 0%, #3a8a5a 45%, #7a2e7a 80%, #c1453a 100%);
    opacity: .85;
  }

  .offer-star { position: absolute; left: 0; top: 0; }
  .offer-text {
    position: absolute; left: 70px; top: 74px; width: 180px;
    transform: rotate(-22deg); transform-origin: center;
    text-align: center; color: var(--berry); font-weight: 700;
    font-size: 12px; line-height: 1.2;
  }

  .brand-site {
    position: absolute; top: 27px; left: 300px; width: 600px; text-align: center;
    color: var(--white); font-size: 36px; font-weight: 600;
  }
  .brand-phone {
    position: absolute; top: 72px; left: 300px; width: 600px; text-align: center;
    color: var(--white); font-size: 27px;
  }
  .tagline-delivery {
    position: absolute; top: 116px; left: 270px; width: 680px; text-align: center;
    color: var(--white); font-size: 38px; font-weight: 700; font-style: italic;
    -webkit-text-stroke: 1px var(--berry-dark);
    transform: rotate(-2.5deg);
  }
  .tagline-quality {
    position: absolute; top: 168px; left: 575px; width: 520px; text-align: center;
    color: var(--white); font-size: 36px; font-style: italic; font-weight: 400;
    transform: rotate(-13deg); transform-origin: center;
  }

  .schedule { position: absolute; left: 424px; top: 392px; width: 390px; }
  .schedule-kicker { text-align: center; color: var(--ink-blue); font-size: 23px; }
  .schedule-title {
    margin: 4px auto 0; width: 300px; height: 40px; background: var(--white);
    color: var(--ink-blue); font-size: 29px; text-align: center; line-height: 39px;
  }
  .schedule-days { display: flex; margin-top: 18px; }
  .day {
    flex: 1; text-align: center; color: var(--ink-blue); font-size: 24px;
    border-left: 2px solid var(--box-border);
  }
  .day:first-child { border-left: none; }
  .day-box {
    display: block; margin: 8px auto 0; width: 28px; height: 28px;
    background: var(--white); border-radius: 3px;
  }

  .price-list { position: absolute; left: 883px; top: 392px; color: var(--list-blue); font-size: 35px; line-height: 42px; }
  .price-list .price { position: absolute; left: 150px; top: 0; }

  .contact-footer {
    position: absolute; left: 312px; top: 630px; width: 600px; text-align: center; color: var(--ink-blue);
  }
  .contact-footer .phone { font-size: 25px; }
  .contact-footer .site { font-size: 31px; }
</style>
</head>
<body>
  <div class="format-label">Flyer 5,5 X 3,5”</div>

  <section class="flyer">
    <svg class="flyer-swoosh" width="1200" height="330" viewBox="0 0 1200 330" aria-hidden="true">
      <path d="M0 0 H1200 V300 C1050 275 800 258 560 258 C330 258 150 220 0 175 Z" fill="var(--berry)"/>
      <path d="M1200 300 C1050 275 800 258 560 258 C330 258 150 220 0 175" fill="none" stroke="var(--white)" stroke-width="10"/>
    </svg>

    <div class="mascot-art" role="img" aria-label="Illustration of a friendly dairy sprite on a flying carpet holding a gallon of milk, with the thedairysprite.com name arced beside it"></div>

    <svg class="offer-star" width="330" height="210" viewBox="0 0 330 210" aria-hidden="true">
      <polygon fill="var(--star)" points="325,100 276,120 303,152 245,154 242,191 191,173 160,205 129,173 78,191 75,154 17,152 44,120 0,100 44,80 17,48 75,46 78,9 129,27 160,0 191,27 242,9 245,46 303,48 276,80"/>
    </svg>
    <p class="offer-text">Free delivery with $10 minimum<br>to your door before breakfast<br>1-800-4567-moo</p>

    <p class="brand-site">thedairysprite.com</p>
    <p class="brand-phone">1-800-moo-4567</p>
    <p class="tagline-delivery">delivered to your door before breakfast</p>
    <p class="tagline-quality">quality, fresh, fully guaranteed</p>

    <div class="schedule">
      <p class="schedule-kicker">free home delivery</p>
      <p class="schedule-title">delivery schedule</p>
      <div class="schedule-days">
        <div class="day">Mon<span class="day-box"></span></div>
        <div class="day">Tue<span class="day-box"></span></div>
        <div class="day">Wed<span class="day-box"></span></div>
        <div class="day">Thu<span class="day-box"></span></div>
        <div class="day">Sat<span class="day-box"></span></div>
        <div class="day">Sun<span class="day-box"></span></div>
      </div>
    </div>

    <div class="price-list">
      <span class="price">$3.99</span>
      Milk<br>Sausag<br>Bacon<br>O.j
    </div>

    <div class="contact-footer">
      <p class="phone">1-800-moo-4567</p>
      <p class="site">thedairysprite.com</p>
    </div>
  </section>
</body>
</html>
```